Coupons App Design Project

We have a simple coupons app with few screens and actions:
1. Very simple login screen (with pinloft and zarvik+)
2. Very simple business search page
3. Very simple business search results(each result contains logo icon, business name and delete icon)
4. business list (every row contains logo icon, business name and delete icon)
5. coupons list (each item contains image, title, subtitle, description, expiration time, status graphics (valid, expired, redeemed), delete icon
6. coupon view (image, title, subtitle, description, barcode etc.)
7. custom confirmation dialog(title, buttons, background, text)
8. "scan to subscribe" page (merchant name, merchant number, background image, text, barcode to scan etc.)
9. simple menu
10. splash screen

all graphics should be vector graphics so we can use it to different resolutions including for printing
Updates

Hi all, We've increased the project's budget by 25%. Thanks

Hi all,

We've decided to change the project from refundable to committed payment.
FYI

Hi All,

Thank you for your time and efforts, we really appreciate it.However we've eliminated most of the offered designs we've received becausethey didn't fit our desired look and feel.

Please download our look and feel file from our uploaded files -we've put there some examples of other apps that we like.

Thanks

Target Market(s)

shoppers all over the world

Industry/Entity Type

Business

Requirements
Must have
• Please take a look at the attached file "look & feel.jpg" for some nice screen shots taken from apps that we like

http://www.briefhatchly.com/file.aspx?fileLocation=storage_url/brief_uploads/166833_09lookandfeel_brief010902.jpg
Should not have
• *****************************************************************************************
The attached files are only for demonstration purpose and needs descriptions so please don't send us design based on these screenshots.
*****************************************************************************************

```html
<!DOCTYPE html>
<html lang="en">
<head>
<meta charset="utf-8">
<title>Coupons App – Business Search and Business List</title>
<link rel="stylesheet" href="https://fonts.googleapis.com/css2?family=Roboto:wght@400;500&display=swap">
<style>
  :root {
    --page-bg: #e3e4e6;
    --status-bg: #141414;
    --status-accent: #33b5e5;
    --bar-bg: #3d4252;
    --bar-text: #ffffff;
    --bar-divider: #575d6e;
    --search-frame: #4f7cb6;
    --search-field: #96c0ef;
    --search-stitch: #2d5488;
    --row-bg: #f8f8f8;
    --thumb-bg: #dadada;
    --thumb-border: #b9b9b9;
    --title-color: #3f6a9c;
    --subtitle-color: #8a8a8a;
    --rule: #bdbdbd;
    --icon-grey: #6b6e78;
    --sep-bg: #ececec;
  }
  * { box-sizing: border-box; margin: 0; padding: 0; }
  html, body { width: 1200px; height: 1000px; overflow: hidden; }
  body {
    background: var(--page-bg);
    font-family: "Roboto", Arial, sans-serif;
    position: relative;
  }
  .screen {
    position: absolute;
    top: 60px;
    width: 480px;
    height: 880px;
    background: var(--row-bg);
    overflow: hidden;
    box-shadow: 0 6px 24px rgba(0,0,0,.18);
  }
  .screen--search { left: 90px; }
  .screen--list { left: 630px; }

  .status-bar {
    height: 26px;
    background: var(--status-bg);
    display: flex;
    justify-content: flex-end;
    align-items: center;
    gap: 6px;
    padding-right: 8px;
    color: var(--status-accent);
    font-size: 17px;
  }
  .action-bar {
    height: 58px;
    background: var(--bar-bg);
    display: flex;
    align-items: center;
    color: var(--bar-text);
    position: relative;
  }
  .action-bar__title {
    font-size: 25px;
    font-weight: 400;
    padding-left: 18px;
    flex: 1;
  }
  .action-bar__user {
    display: flex; align-items: center; gap: 8px;
    font-size: 19px; padding: 0 14px;
  }
  .action-bar__item {
    height: 58px; width: 56px;
    display: flex; align-items: center; justify-content: center;
    border-left: 1px solid var(--bar-divider);
  }

  .search-panel {
    position: absolute;
    top: 84px; left: 0; right: 0;
    height: 128px;
    background: var(--search-frame);
    padding: 10px;
    z-index: 2;
    box-shadow: 0 3px 6px rgba(0,0,0,.25);
  }
  .search-panel::before {
    content: ""; position: absolute; inset: 4px;
    border: 1px dashed var(--search-stitch);
  }
  .search-panel__notch {
    position: absolute; top: -8px; right: 74px;
    width: 16px; height: 16px; background: var(--search-frame);
    transform: rotate(45deg);
  }
  .search-field {
    position: relative;
    height: 100%;
    background: var(--search-field);
    border-radius: 3px;
    padding: 10px 12px;
    display: flex;
    align-items: flex-start;
    gap: 10px;
    font-size: 26px;
    color: #1e2a3a;
  }
  .search-field__caret { border-right: 2px solid #1e2a3a; padding-right: 2px; }
  .search-field__clear {
    position: absolute; right: 10px; bottom: 10px;
  }

  .item-list { list-style: none; }
  .screen--search .item-list { padding-top: 140px; }
  .item {
    height: 130px;
    display: flex;
    align-items: center;
    padding: 0 16px 0 14px;
    position: relative;
  }
  .item__thumb {
    width: 100px; height: 100px;
    background: var(--thumb-bg);
    border: 1px solid var(--thumb-border);
    border-radius: 2px;
    flex: none;
    margin-right: 16px;
  }
  .item__text {
    flex: 1;
    align-self: stretch;
    padding-top: 26px;
    border-bottom: 1px dashed var(--rule);
    margin-bottom: 14px;
    margin-right: 40px;
  }
  .item__title { color: var(--title-color); font-size: 24px; font-weight: 500; }
  .item__subtitle { color: var(--subtitle-color); font-size: 18px; margin-top: 2px; }
  .item__chevron { position: absolute; right: 18px; top: 50px; }
  .item__delete { position: absolute; right: 16px; bottom: 10px; }

  .cut-line {
    height: 24px;
    background: var(--sep-bg);
    position: relative;
    border-top: 1px dashed #a5a5a5;
    border-bottom: 1px dashed #a5a5a5;
  }
  .cut-line__zigzag { position: absolute; left: 0; right: 0; top: 8px; }
  .cut-line__scissors { position: absolute; left: 84px; top: -10px; background: var(--row-bg); padding: 0 3px; }
</style>
</head>
<body>

<svg width="0" height="0" style="position:absolute" aria-hidden="true">
  <defs>
    <pattern id="zigzag" width="8" height="6" patternUnits="userSpaceOnUse">
      <path d="M0 5 L4 1 L8 5" fill="none" stroke="#8d8d8d" stroke-width="1"/>
    </pattern>
    <symbol id="icon-chevron" viewBox="0 0 14 20"><path d="M3 3 L11 10 L3 17" fill="none" stroke="#6b6e78" stroke-width="4"/></symbol>
    <symbol id="icon-trash" viewBox="0 0 24 26">
      <rect x="2" y="3" width="20" height="3" rx="1" fill="#6b6e78"/>
      <rect x="9" y="0.5" width="6" height="3" fill="#6b6e78"/>
      <path d="M4 8 H20 L18.5 25 H5.5 Z" fill="none" stroke="#6b6e78" stroke-width="2.2"/>
      <path d="M9 11 V22 M12 11 V22 M15 11 V22" stroke="#6b6e78" stroke-width="1.6"/>
    </symbol>
    <symbol id="icon-scissors" viewBox="0 0 28 18">
      <circle cx="5" cy="4" r="3.2" fill="none" stroke="#333" stroke-width="1.8"/>
      <circle cx="5" cy="14" r="3.2" fill="none" stroke="#333" stroke-width="1.8"/>
      <path d="M8 6 L27 15 M8 12 L27 3" stroke="#333" stroke-width="1.8"/>
    </symbol>
    <symbol id="icon-user" viewBox="0 0 26 26">
      <circle cx="13" cy="8" r="6" fill="#fff"/>
      <path d="M2 26 C2 17 24 17 24 26 Z" fill="#fff"/>
    </symbol>
    <symbol id="icon-search" viewBox="0 0 26 26">
      <circle cx="10" cy="10" r="7" fill="none" stroke="currentColor" stroke-width="3"/>
      <path d="M15 15 L24 24" stroke="currentColor" stroke-width="4" stroke-linecap="round"/>
    </symbol>
    <symbol id="icon-overflow" viewBox="0 0 8 26">
      <rect x="1" y="1" width="6" height="6" fill="#fff"/>
      <rect x="1" y="10" width="6" height="6" fill="#fff"/>
      <rect x="1" y="19" width="6" height="6" fill="#fff"/>
    </symbol>
  </defs>
</svg>

<!-- Business Search screen -->
<section class="screen screen--search">
  <div class="status-bar">
    <svg width="20" height="16" viewBox="0 0 20 16"><path d="M1 15 H19 V1 Z" fill="#33b5e5"/></svg>
    <svg width="10" height="18" viewBox="0 0 10 18"><rect x="3" y="0" width="4" height="2" fill="#33b5e5"/><rect x="0" y="2" width="10" height="16" fill="#33b5e5"/></svg>
    <span>10:07</span>
  </div>
  <header class="action-bar">
    <h1 class="action-bar__title">Business Search</h1>
    <div class="action-bar__user"><svg width="24" height="24"><use href="#icon-user"/></svg>User</div>
    <div class="action-bar__item" style="color:var(--status-accent)"><svg width="26" height="26"><use href="#icon-search"/></svg></div>
    <div class="action-bar__item"><svg width="8" height="26"><use href="#icon-overflow"/></svg></div>
  </header>

  <div class="search-panel">
    <span class="search-panel__notch"></span>
    <div class="search-field">
      <svg width="26" height="26" style="color:#1e2a3a;margin-top:4px"><use href="#icon-search"/></svg>
      <span class="search-field__caret">Lorem</span>
      <svg class="search-field__clear" width="34" height="34" viewBox="0 0 34 34">
        <circle cx="17" cy="17" r="16" fill="#fff"/>
        <path d="M11 11 L23 23 M23 11 L11 23" stroke="#4f7cb6" stroke-width="4"/>
      </svg>
    </div>
  </div>

  <ul class="item-list">
    <li class="item"><div class="item__thumb" role="img" aria-label="Business logo"></div><div class="item__text"><p class="item__title">Item Title</p><p class="item__subtitle">Subtitle</p></div><svg class="item__chevron" width="14" height="20"><use href="#icon-chevron"/></svg><svg class="item__delete" width="24" height="26"><use href="#icon-trash"/></svg></li>
    <li class="cut-line"><svg class="cut-line__zigzag" width="480" height="6"><rect width="480" height="6" fill="url(#zigzag)"/></svg><svg class="cut-line__scissors" width="30" height="18"><use href="#icon-scissors"/></svg></li>
    <li class="item"><div class="item__thumb" role="img" aria-label="Business logo"></div><div class="item__text"><p class="item__title">Item Title</p><p class="item__subtitle">Subtitle</p></div><svg class="item__chevron" width="14" height="20"><use href="#icon-chevron"/></svg><svg class="item__delete" width="24" height="26"><use href="#icon-trash"/></svg></li>
    <li class="cut-line"><svg class="cut-line__zigzag" width="480" height="6"><rect width="480" height="6" fill="url(#zigzag)"/></svg><svg class="cut-line__scissors" width="30" height="18"><use href="#icon-scissors"/></svg></li>
    <li class="item"><div class="item__thumb" role="img" aria-label="Business logo"></div><div class="item__text"><p class="item__title">Item Title</p><p class="item__subtitle">Subtitle</p></div><svg class="item__chevron" width="14" height="20"><use href="#icon-chevron"/></svg><svg class="item__delete" width="24" height="26"><use href="#icon-trash"/></svg></li>
    <li class="cut-line"><svg class="cut-line__zigzag" width="480" height="6"><rect width="480" height="6" fill="url(#zigzag)"/></svg><svg class="cut-line__scissors" width="30" height="18"><use href="#icon-scissors"/></svg></li>
    <li class="item"><div class="item__thumb" role="img" aria-label="Business logo"></div><div class="item__text"><p class="item__title">Item Title</p><p class="item__subtitle">Subtitle</p></div><svg class="item__chevron" width="14" height="20"><use href="#icon-chevron"/></svg><svg class="item__delete" width="24" height="26"><use href="#icon-trash"/></svg></li>
    <li class="cut-line"><svg class="cut-line__zigzag" width="480" height="6"><rect width="480" height="6" fill="url(#zigzag)"/></svg><svg class="cut-line__scissors" width="30" height="18"><use href="#icon-scissors"/></svg></li>
    <li class="item"><div class="item__thumb" role="img" aria-label="Business logo"></div><div class="item__text"><p class="item__title">Item Title</p><p class="item__subtitle">Subtitle</p></div><svg class="item__chevron" width="14" height="20"><use href="#icon-chevron"/></svg><svg class="item__delete" width="24" height="26"><use href="#icon-trash"/></svg></li>
  </ul>
</section>

<!-- Business List screen -->
<section class="screen screen--list">
  <div class="status-bar">
    <svg width="20" height="16" viewBox="0 0 20 16"><path d="M1 15 H19 V1 Z" fill="#33b5e5"/></svg>
    <svg width="10" height="18" viewBox="0 0 10 18"><rect x="3" y="0" width="4" height="2" fill="#33b5e5"/><rect x="0" y="2" width="10" height="16" fill="#33b5e5"/></svg>
    <span>10:07</span>
  </div>
  <header class="action-bar">
    <h1 class="action-bar__title">Business List</h1>
    <div class="action-bar__user"><svg width="24" height="24"><use href="#icon-user"/></svg>User</div>
    <div class="action-bar__item" style="color:#fff"><svg width="26" height="26"><use href="#icon-search"/></svg></div>
    <div class="action-bar__item"><svg width="8" height="26"><use href="#icon-overflow"/></svg></div>
  </header>

  <ul class="item-list">
    <li class="item"><div class="item__thumb" role="img" aria-label="Business logo"></div><div class="item__text"><p class="item__title">Item Title</p><p class="item__subtitle">Subtitle</p></div><svg class="item__chevron" width="14" height="20"><use href="#icon-chevron"/></svg><svg class="item__delete" width="24" height="26"><use href="#icon-trash"/></svg></li>
    <li class="cut-line"><svg class="cut-line__zigzag" width="480" height="6"><rect width="480" height="6" fill="url(#zigzag)"/></svg><svg class="cut-line__scissors" width="30" height="18"><use href="#icon-scissors"/></svg></li>
    <li class="item"><div class="item__thumb" role="img" aria-label="Business logo"></div><div class="item__text"><p class="item__title">Item Title</p><p class="item__subtitle">Subtitle</p></div><svg class="item__chevron" width="14" height="20"><use href="#icon-chevron"/></svg><svg class="item__delete" width="24" height="26"><use href="#icon-trash"/></svg></li>
    <li class="cut-line"><svg class="cut-line__zigzag" width="480" height="6"><rect width="480" height="6" fill="url(#zigzag)"/></svg><svg class="cut-line__scissors" width="30" height="18"><use href="#icon-scissors"/></svg></li>
    <li class="item"><div class="item__thumb" role="img" aria-label="Business logo"></div><div class="item__text"><p class="item__title">Item Title</p><p class="item__subtitle">Subtitle</p></div><svg class="item__chevron" width="14" height="20"><use href="#icon-chevron"/></svg><svg class="item__delete" width="24" height="26"><use href="#icon-trash"/></svg></li>
    <li class="cut-line"><svg class="cut-line__zigzag" width="480" height="6"><rect width="480" height="6" fill="url(#zigzag)"/></svg><svg class="cut-line__scissors" width="30" height="18"><use href="#icon-scissors"/></svg></li>
    <li class="item"><div class="item__thumb" role="img" aria-label="Business logo"></div><div class="item__text"><p class="item__title">Item Title</p><p class="item__subtitle">Subtitle</p></div><svg class="item__chevron" width="14" height="20"><use href="#icon-chevron"/></svg><svg class="item__delete" width="24" height="26"><use href="#icon-trash"/></svg></li>
    <li class="cut-line"><svg class="cut-line__zigzag" width="480" height="6"><rect width="480" height="6" fill="url(#zigzag)"/></svg><svg class="cut-line__scissors" width="30" height="18"><use href="#icon-scissors"/></svg></li>
    <li class="item"><div class="item__thumb" role="img" aria-label="Business logo"></div><div class="item__text"><p class="item__title">Item Title</p><p class="item__subtitle">Subtitle</p></div><svg class="item__chevron" width="14" height="20"><use href="#icon-chevron"/></svg><svg class="item__delete" width="24" height="26"><use href="#icon-trash"/></svg></li>
  </ul>
</section>

</body>
</html>
```